Stonebay Towing Business Card

Towing
Accident towing
Mechanical breakdown
Insurance, salvage and recovery
4wd off road towing
Light & Heavy towing
8347 2516
24 hour business 7 days

Logo can be whole size on front

Industry/Entity Type

Towing/ transport

Contact Information for Business Card

The above

```html
<!DOCTYPE html>
<html lang="en">
<head>
<meta charset="utf-8">
<title>Stonebay Towing Business Card</title>
<link href="https://fonts.googleapis.com/css2?family=Saira:ital,wght@0,600;0,700;0,800;1,600;1,700;1,800&display=swap" rel="stylesheet">
<style>
  :root {
    --page: #1b1d22;
    --card-dark: #0d0d0f;
    --card-mid: #1c1d20;
    --red: #d42027;
    --red-deep: #a8141a;
    --white: #ffffff;
    --grey: #c9c9c9;
  }
  * { margin: 0; padding: 0; box-sizing: border-box; }
  html, body {
    width: 1200px; height: 900px; overflow: hidden;
    background: var(--page);
    font-family: "Saira", sans-serif;
  }
  .canvas { position: relative; width: 1200px; height: 900px; }
  .card {
    position: absolute; left: 250px; width: 700px; height: 400px;
    overflow: hidden; border-radius: 2px;
    box-shadow: 0 14px 36px rgba(0,0,0,0.55);
  }
  .card-front { top: 35px; }
  .card-back { top: 465px; }
  .mesh-texture {
    position: absolute; inset: 0;
    background: radial-gradient(ellipse at 40% 40%, var(--card-mid) 0%, var(--card-dark) 75%);
  }
  .brand-name {
    position: absolute; color: var(--red); font-weight: 800;
    text-transform: uppercase; letter-spacing: 1px; line-height: 1;
  }
  .card-front .brand-name {
    left: 0; right: 0; top: 70px; text-align: center; font-size: 62px; white-space: nowrap;
  }
  .services-heading {
    position: absolute; left: 50%; top: 200px; transform: translateX(-50%);
    padding: 2px 60px; font-size: 18px; font-weight: 700; font-style: italic;
    color: var(--white); letter-spacing: 1px; white-space: nowrap;
    background: linear-gradient(90deg, transparent, var(--red-deep) 25%, var(--red-deep) 75%, transparent);
  }
  .services-list {
    position: absolute; left: 0; right: 0; top: 240px; list-style: none;
    text-align: center; color: var(--white); font-style: italic; font-weight: 700;
    font-size: 21px; line-height: 1.38; letter-spacing: 0.6px;
  }
  .card-back .brand-name {
    left: 20px; top: 95px; width: 300px; text-align: center;
    font-size: 46px; line-height: 1.05;
  }
  .brand-line { display: block; white-space: nowrap; }
  .divider {
    position: absolute; left: 340px; top: 60px; width: 2px; height: 220px;
    background: var(--grey); transform: rotate(4deg);
  }
  .contact { position: absolute; left: 372px; top: 62px; }
  .contact-name {
    color: var(--red); font-weight: 800; font-style: italic; font-size: 26px; letter-spacing: 1px;
  }
  .contact-role {
    color: var(--white); font-weight: 700; font-style: italic; font-size: 19px; margin-top: -6px;
  }
  .contact-phone {
    display: flex; align-items: center; gap: 10px; margin-top: 26px;
    color: var(--white); font-weight: 700; font-style: italic; font-size: 22px; letter-spacing: 1px;
  }
  .hours-big {
    margin-top: 12px; color: var(--red); font-weight: 800; font-style: italic; font-size: 50px; line-height: 1;
  }
  .hours-small {
    color: var(--white); font-weight: 700; font-style: italic; font-size: 28px; line-height: 1.1;
  }
  .swoosh { position: absolute; left: 0; bottom: 0; width: 700px; height: 150px; }
</style>
</head>
<body>
<main class="canvas">
  <section class="card card-front">
    <div class="mesh-texture" role="img" aria-label="Dark carbon hexagon mesh texture"></div>
    <h1 class="brand-name">Stonebay Towing</h1>
    <h2 class="services-heading">OUR SERVICES</h2>
    <ul class="services-list">
      <li>Accident towing | Mechanical breakdown</li>
      <li>Insurance, salvage and recovery</li>
      <li>4wd off road towing &nbsp;|&nbsp; Light &amp; Heavy towing</li>
    </ul>
  </section>

  <section class="card card-back">
    <div class="mesh-texture" role="img" aria-label="Dark carbon hexagon mesh texture"></div>
    <svg class="swoosh" viewBox="0 0 700 150" preserveAspectRatio="none" aria-hidden="true">
      <path d="M0 30 C40 110 250 118 470 112 L470 116 C250 126 40 122 0 60 Z" fill="var(--white)"/>
      <path d="M0 62 C60 130 300 132 700 96 L700 150 L0 150 Z" fill="var(--red)"/>
    </svg>
    <div class="brand-name">
      <span class="brand-line">Stonebay</span>
      <span class="brand-line">Towing</span>
    </div>
    <div class="divider"></div>
    <div class="contact">
      <p class="contact-name">MARCUS REILLY</p>
      <p class="contact-role">Manager</p>
      <p class="contact-phone">
        <svg width="22" height="20" viewBox="0 0 24 22" aria-hidden="true">
          <path d="M2 7 C2 3 22 3 22 7 L22 9 L17 9 L17 6.5 L7 6.5 L7 9 L2 9 Z" fill="var(--red)"/>
          <path d="M6 10 L18 10 L21 20 L3 20 Z" fill="var(--red)"/>
          <circle cx="12" cy="15" r="2.6" fill="var(--card-dark)"/>
        </svg>
        8347 2516
      </p>
      <p class="hours-big">24 hour</p>
      <p class="hours-small">business 7 days</p>
    </div>
  </section>
</main>
</body>
</html>
```